Re-Design the flow of the Orvane Framework

The orvane framework is a 10 step model that helps teams/organizations become high performing. Attached the model which i created. I love the design as it is but i used a template i don't owe the rights of so i would like to use this platform to see what you can come up with the redesign this flow while keeping the key elements in place. I like the flow, i like the cleanness and i like it to be compact.

Target Market(s)

Organizational change / Leadership/ Consultancy

Industry/Entity Type

Leadership

Requirements
Must have
• Keep as much as possible the flow and feel of the attached
Nice to have
• -Maybe some twist in how the different parts connect (not a must)
Should not have
• Less or more steps than added in the attached file

```html
<!DOCTYPE html>
<html lang="en">
<head>
<meta charset="utf-8">
<title>The Orvane Framework</title>
<link rel="stylesheet" href="https://fonts.googleapis.com/css2?family=Titillium+Web:ital,wght@0,400;0,600;0,700;1,300;1,400&family=Raleway:wght@200&display=swap">
<style>
  :root {
    --bg-light: #eceded;
    --bg-dark: #c6c7c9;
    --ink: #555658;
    --ink-dark: #2e2f31;
    --accent: #1d9bd7;
    --panel: #f2f2f3;
    --flow: rgba(255,255,255,0.6);
    --globe-core: #d2d3d5;
    --globe-edge: #e4e5e6;
    --c01: #f5c400;
    --c02: #f07a1a;
    --c03: #e8336e;
    --c04: #9c2f8f;
    --c05: #5b3f97;
    --c06: #4a5ba8;
    --c07: #0f6cb8;
    --c08: #1ea4e0;
    --c09: #37b9be;
    --c10: #a9cd37;
    --row-icon: #9a9b9d;
  }
  html, body { margin: 0; padding: 0; overflow: hidden; }
  body { width: 1200px; height: 996px; background: var(--bg-light); }
  .canvas { display: block; width: 1200px; height: 996px; }
  .title { font-family: "Titillium Web", sans-serif; font-weight: 700; font-size: 84px; fill: var(--ink); }
  .title .brand { fill: var(--accent); }
  .subtitle { font-family: "Titillium Web", sans-serif; font-weight: 400; font-size: 23px; fill: var(--ink); }
  .arc-label { font-family: "Titillium Web", sans-serif; font-weight: 700; font-size: 50px; fill: var(--ink); letter-spacing: 1px; }
  .step-num { font-family: "Raleway", sans-serif; font-weight: 200; font-size: 50px; }
  .step-text { font-family: "Titillium Web", sans-serif; font-style: italic; font-weight: 300; font-size: 17px; fill: var(--ink-dark); }
  .goal-head { font-family: "Titillium Web", sans-serif; font-style: italic; font-weight: 400; font-size: 21px; fill: var(--ink-dark); }
  .goal-list { font-family: "Titillium Web", sans-serif; font-style: italic; font-weight: 300; font-size: 15.5px; fill: var(--ink-dark); }
  .panel { fill: var(--panel); }
  .panels { filter: drop-shadow(3px 4px 5px rgba(0,0,0,0.16)); }
  .ring-icon { color: #fff; }
  .ring-frame { fill: none; stroke: #fff; stroke-width: 1.5; }
  .row-icon { color: var(--row-icon); }
  .row-ring { fill: none; stroke: #c3c4c6; stroke-width: 1.5; }
  .arrow-glyph { fill: var(--ink); }
</style>
</head>
<body>
<svg class="canvas" viewBox="0 0 1600 1328" xmlns="http://www.w3.org/2000/svg">
  <defs>
    <radialGradient id="bg-grad" cx="50%" cy="40%" r="75%">
      <stop offset="0" stop-color="var(--bg-light)"/>
      <stop offset="1" stop-color="var(--bg-dark)"/>
    </radialGradient>
    <radialGradient id="globe-grad" cx="50%" cy="55%" r="50%">
      <stop offset="0" stop-color="var(--globe-core)"/>
      <stop offset="1" stop-color="var(--globe-edge)"/>
    </radialGradient>
    <radialGradient id="ring-shade" cx="50%" cy="50%" r="50%">
      <stop offset="0.55" stop-color="#000" stop-opacity="0.18"/>
      <stop offset="1" stop-color="#000" stop-opacity="0"/>
    </radialGradient>

    <path id="arc-top" d="M25,785 A455 455 0 0 1 935,785"/>
    <path id="arc-bottom" d="M650,805 A470 470 0 0 0 1590,805"/>

    <path id="top-panel" d="M-64.05,-203.1 L-128.7,-408.2 A428 428 0 0 1 128.7,-408.2 L64.05,-203.1 A213 213 0 0 0 -64.05,-203.1 Z"/>
    <path id="top-seg" d="M-65.8,-202.6 A213 213 0 0 1 65.8,-202.6 L40.2,-123.6 A130 130 0 0 0 -40.2,-123.6 Z"/>
    <path id="bottom-panel" d="M-61.6,195.5 L-128.7,408.2 A428 428 0 0 0 128.7,408.2 L61.6,195.5 A205 205 0 0 1 -61.6,195.5 Z"/>
    <path id="bottom-seg" d="M-63.3,195 A205 205 0 0 0 63.3,195 L38.6,118.9 A125 125 0 0 1 -38.6,118.9 Z"/>

    <symbol id="i-home" viewBox="-12 -12 24 24"><polygon points="0,-9 10,0 6.5,0 6.5,8 2,8 2,3 -2,3 -2,8 -6.5,8 -6.5,0 -10,0" fill="currentColor"/></symbol>
    <symbol id="i-bulb" viewBox="-12 -12 24 24"><g fill="none" stroke="currentColor" stroke-width="1.8"><circle cx="0" cy="-3" r="5.5"/><path d="M-2.5,3 V6 H2.5 V3"/><path d="M-2,9 H2"/></g></symbol>
    <symbol id="i-chat" viewBox="-12 -12 24 24"><rect x="-9" y="-8" width="18" height="12" rx="2" fill="currentColor"/><polygon points="-3,4 0,9 2,4" fill="currentColor"/></symbol>
    <symbol id="i-hand" viewBox="-12 -12 24 24"><g fill="none" stroke="currentColor" stroke-width="1.7"><circle cx="1" cy="-4" r="4.5"/><path d="M-10,7 Q-5,2 0,5 L8,2"/><path d="M-10,10 H3 L9,5"/></g></symbol>
    <symbol id="i-mail" viewBox="-12 -12 24 24"><g fill="none" stroke="currentColor" stroke-width="1.7"><rect x="-9" y="-6.5" width="18" height="13"/><polyline points="-9,-6.5 0,1 9,-6.5"/></g></symbol>
    <symbol id="i-clock" viewBox="-12 -12 24 24"><g fill="none" stroke="currentColor" stroke-width="1.7"><circle r="8.5"/><path d="M0,-5 V0 H4"/></g></symbol>
    <symbol id="i-cash" viewBox="-12 -12 24 24"><g fill="none" stroke="currentColor" stroke-width="1.7"><rect x="-10" y="-6" width="20" height="12" rx="1"/><circle r="3"/></g></symbol>
    <symbol id="i-gear" viewBox="-12 -12 24 24"><g fill="none" stroke="currentColor"><circle r="6.5" stroke-width="3.5" stroke-dasharray="2.6 2.5"/><circle r="3" stroke-width="1.8"/></g></symbol>
    <symbol id="i-chart" viewBox="-12 -12 24 24"><g fill="currentColor"><rect x="-9" y="2" width="3" height="6"/><rect x="-4.5" y="-1" width="3" height="9"/><rect x="0" y="-4" width="3" height="12"/><rect x="4.5" y="-8" width="3" height="16"/></g></symbol>
    <symbol id="i-team" viewBox="-12 -12 24 24"><g fill="currentColor"><circle cx="-5" cy="-2" r="3"/><circle cx="5" cy="-2" r="3"/><rect x="-9" y="2" width="8" height="7" rx="2"/><rect x="1" y="2" width="8" height="7" rx="2"/><rect x="-3" y="-11" width="6" height="4" rx="1"/></g></symbol>
  </defs>

  <!-- backdrop -->
  <rect width="1600" height="1328" fill="url(#bg-grad)"/>

  <!-- globe area -->
  <circle cx="480" cy="800" r="315" fill="url(#globe-grad)" role="img" aria-label="Dotted world map showing global reach"/>

  <!-- connecting flow: loop back from step 10 to step 01, through the centre -->
  <g class="flow">
    <path d="M205,905 C205,1110 320,1215 470,1215 C630,1215 750,1110 810,960 C870,800 930,560 1005,420 C1075,290 1245,255 1320,360 L1395,455" fill="none" stroke="var(--flow)" stroke-width="200" stroke-linecap="butt"/>
    <polygon points="50,915 205,800 360,915" fill="var(--flow)"/>
  </g>

  <!-- goal arrow -->
  <g class="panels">
    <polygon class="panel" points="1215,445 1400,338 1585,445 1545,445 1545,785 1253,785 1253,445"/>
  </g>
  <g class="goal">
    <g fill="none" stroke="#111" stroke-width="4" stroke-linejoin="round">
      <path d="M1374,440 H1422 L1440,462 L1398,512 L1356,462 Z"/>
      <path d="M1356,462 H1440"/>
      <path d="M1386,440 L1378,462 L1398,512 L1418,462 L1410,440"/>
    </g>
    <text class="goal-head" x="1398" y="573" text-anchor="middle">Reaching full potential of</text>
    <text class="goal-head" x="1398" y="596" text-anchor="middle">people and organization</text>
    <g fill="#333">
      <circle cx="1283" cy="637" r="2.5"/><circle cx="1283" cy="659" r="2.5"/>
      <circle cx="1283" cy="681" r="2.5"/><circle cx="1283" cy="703" r="2.5"/>
    </g>
    <text class="goal-list" x="1320" y="642">Productivity up to 800%</text>
    <text class="goal-list" x="1320" y="664">Employee engagement &gt;90%</text>
    <text class="goal-list" x="1320" y="686">Max discretionary effort gap</text>
    <text class="goal-list" x="1320" y="708">High resilience to change</text>
  </g>

  <!-- top fan: steps 01-05 -->
  <g transform="translate(480,785)">
    <g class="panels">
      <use href="#top-panel" class="panel" transform="rotate(-72)"/>
      <use href="#top-panel" class="panel" transform="rotate(-36)"/>
      <use href="#top-panel" class="panel"/>
      <use href="#top-panel" class="panel" transform="rotate(36)"/>
      <use href="#top-panel" class="panel" transform="rotate(72)"/>
    </g>
    <use href="#top-seg" fill="var(--c01)" transform="rotate(-72)"/>
    <use href="#top-seg" fill="var(--c02)" transform="rotate(-36)"/>
    <use href="#top-seg" fill="var(--c03)"/>
    <use href="#top-seg" fill="var(--c04)" transform="rotate(36)"/>
    <use href="#top-seg" fill="var(--c05)" transform="rotate(72)"/>
    <path d="M-213,0 A213 213 0 0 1 213,0 L130,0 A130 130 0 0 0 -130,0 Z" fill="url(#ring-shade)" opacity="0.5"/>
  </g>
  <g class="ring-frame">
    <circle cx="317" cy="740" r="21"/><circle cx="379" cy="655" r="21"/>
    <circle cx="480" cy="622" r="21"/><circle cx="581" cy="655" r="21"/>
    <circle cx="643" cy="740" r="21"/>
  </g>
  <g class="ring-icon">
    <use href="#i-home" x="307" y="730" width="20" height="20"/>
    <use href="#i-bulb" x="369" y="645" width="20" height="20"/>
    <use href="#i-chat" x="470" y="612" width="20" height="20"/>
    <use href="#i-hand" x="571" y="645" width="20" height="20"/>
    <use href="#i-mail" x="633" y="730" width="20" height="20"/>
  </g>

  <g class="steps-top">
    <text class="step-num" x="94" y="712" fill="var(--c01)">01</text>
    <text class="step-text" x="252" y="692" text-anchor="end">Discover your</text>
    <text class="step-text" x="252" y="712" text-anchor="end">purpose. Why</text>
    <text class="step-text" x="252" y="732" text-anchor="end">Do you exist?</text>

    <text class="step-num" x="202" y="557" fill="var(--c02)">02</text>
    <text class="step-text" x="277" y="530">Identify</text>
    <text class="step-text" x="277" y="550">Purpose</text>
    <text class="step-text" x="277" y="570">Activators</text>
    <text class="step-text" x="277" y="590">(Vision)</text>

    <text class="step-num" x="394" y="488" fill="var(--c03)">03</text>
    <text class="step-text" x="472" y="462">Develop a</text>
    <text class="step-text" x="472" y="480">Master plan</text>
    <text class="step-text" x="472" y="498">(strategy)</text>

    <text class="step-num" x="577" y="556" fill="var(--c04)">04</text>
    <text class="step-text" x="653" y="515">Cultivate</text>
    <text class="step-text" x="653" y="535">Psychological</text>
    <text class="step-text" x="653" y="555">Safety and</text>
    <text class="step-text" x="653" y="575">Ownership</text>

    <text class="step-num" x="703" y="710" fill="var(--c05)">05</text>
    <text class="step-text" x="776" y="678">Tap into peoples</text>
    <text class="step-text" x="776" y="696">Purpose and</text>
    <text class="step-text" x="776" y="714">Passion (intrinsic</text>
    <text class="step-text" x="776" y="732">motivation)</text>
  </g>

  <!-- bottom fan: steps 06-10 -->
  <g transform="translate(1120,805)">
    <g class="panels">
      <use href="#bottom-panel" class="panel" transform="rotate(72)"/>
      <use href="#bottom-panel" class="panel" transform="rotate(36)"/>
      <use href="#bottom-panel" class="panel"/>
      <use href="#bottom-panel" class="panel" transform="rotate(-36)"/>
      <use href="#bottom-panel" class="panel" transform="rotate(-72)"/>
    </g>
    <use href="#bottom-seg" fill="var(--c06)" transform="rotate(72)"/>
    <use href="#bottom-seg" fill="var(--c07)" transform="rotate(36)"/>
    <use href="#bottom-seg" fill="var(--c08)"/>
    <use href="#bottom-seg" fill="var(--c09)" transform="rotate(-36)"/>
    <use href="#bottom-seg" fill="var(--c10)" transform="rotate(-72)"/>
  </g>
  <g class="ring-frame">
    <circle cx="963" cy="856" r="21"/><circle cx="1023" cy="938" r="21"/>
    <circle cx="1120" cy="970" r="21"/><circle cx="1217" cy="938" r="21"/>
    <circle cx="1277" cy="856" r="21"/>
  </g>
  <g class="ring-icon">
    <use href="#i-clock" x="953" y="846" width="20" height="20"/>
    <use href="#i-cash" x="1013" y="928" width="20" height="20"/>
    <use href="#i-gear" x="1110" y="960" width="20" height="20"/>
    <use href="#i-chart" x="1207" y="928" width="20" height="20"/>
    <use href="#i-team" x="1267" y="846" width="20" height="20"/>
  </g>

  <g class="steps-bottom">
    <text class="step-num" x="722" y="907" fill="var(--c06)">06</text>
    <text class="step-text" x="798" y="881">Unlock culture of</text>
    <text class="step-text" x="798" y="901">personal growth</text>
    <text class="step-text" x="798" y="921">&amp; development</text>

    <text class="step-num" x="828" y="1082" fill="var(--c07)">07</text>
    <text class="step-text" x="908" y="1035">Prioritize</text>
    <text class="step-text" x="908" y="1054">Feedback &amp;</text>
    <text class="step-text" x="908" y="1073">Transparency</text>

    <text class="step-num" x="1034" y="1143" fill="var(--c08)">08</text>
    <text class="step-text" x="1109" y="1131">Empower the</text>
    <text class="step-text" x="1109" y="1150">community from</text>
    <text class="step-text" x="1109" y="1169">bottom-up</text>

    <text class="step-num" x="1234" y="1081" fill="var(--c09)">09</text>
    <text class="step-text" x="1253" y="1103">Put excellent (team)</text>
    <text class="step-text" x="1253" y="1123">performance in</text>
    <text class="step-text" x="1253" y="1143">the spotlight</text>

    <text class="step-num" x="1341" y="909" fill="var(--c10)">10</text>
    <text class="step-text" x="1398" y="880">Monitor</text>
    <text class="step-text" x="1398" y="900">engagement</text>
    <text class="step-text" x="1398" y="920">Real-time</text>
  </g>

  <!-- phase labels -->
  <text class="arc-label"><textPath href="#arc-top" startOffset="155">SELF DIRECTION</textPath></text>
  <text class="arc-label"><textPath href="#arc-top" startOffset="784">HUMAN EXPERIENCE</textPath></text>
  <text class="arc-label"><textPath href="#arc-bottom" startOffset="698">UNLEASH ENGAGEMENT</textPath></text>

  <g class="arrow-glyph">
    <g transform="translate(315,362) rotate(-22)">
      <rect x="-28" y="-8" width="36" height="16"/><polygon points="8,-20 34,0 8,20"/>
    </g>
    <g transform="translate(924,698) rotate(88)">
      <rect x="-28" y="-8" width="36" height="16"/><polygon points="8,-20 34,0 8,20"/>
    </g>
    <g transform="translate(1553,948) rotate(-82)">
      <rect x="-22" y="-7" width="30" height="14"/><polygon points="8,-17 30,0 8,17"/>
    </g>
  </g>

  <!-- title -->
  <text class="title" x="800" y="150" text-anchor="middle">THE <tspan class="brand">ORVANE</tspan> FRAMEWORK</text>
  <text class="subtitle" x="800" y="185" text-anchor="middle">LIBERATE THE WORKPLACE UNLEASHING VALUE THROUG PURPOSE AT EVERY LEVEL OF SCALE</text>

  <!-- step icon row -->
  <g class="icon-row">
    <circle class="row-ring" cx="266" cy="1302" r="22"/>
    <circle class="row-ring" cx="385" cy="1302" r="22"/>
    <circle class="row-ring" cx="503" cy="1302" r="22"/>
    <circle class="row-ring" cx="622" cy="1302" r="22"/>
    <circle class="row-ring" cx="740" cy="1302" r="22"/>
    <circle class="row-ring" cx="858" cy="1302" r="22"/>
    <circle class="row-ring" cx="977" cy="1302" r="22"/>
    <circle class="row-ring" cx="1095" cy="1302" r="22"/>
    <circle class="row-ring" cx="1213" cy="1302" r="22"/>
    <circle class="row-ring" cx="1332" cy="1302" r="22"/>
    <g class="row-icon">
      <use href="#i-home" x="256" y="1292" width="20" height="20"/>
      <use href="#i-bulb" x="375" y="1292" width="20" height="20"/>
      <use href="#i-chat" x="493" y="1292" width="20" height="20"/>
      <use href="#i-hand" x="612" y="1292" width="20" height="20"/>
      <use href="#i-mail" x="730" y="1292" width="20" height="20"/>
      <use href="#i-clock" x="848" y="1292" width="20" height="20"/>
      <use href="#i-cash" x="967" y="1292" width="20" height="20"/>
      <use href="#i-gear" x="1085" y="1292" width="20" height="20"/>
      <use href="#i-chart" x="1203" y="1292" width="20" height="20"/>
      <use href="#i-team" x="1322" y="1292" width="20" height="20"/>
    </g>
  </g>
</svg>
</body>
</html>
```